Halvorsen Partners Business Card

Halvorsen Partners Civil Construction
Marcus Halvorsen
CEO
727-518-6094
Marcus@HalvorsenSiteworks.example
www.HalvorsenSiteworks.example
Site Development
Utility Construction
Excavation
40876 County Lane 19
Land O' Lakes, FL 34638

Target Market(s)

Construction and government

Industry/Entity Type

Business

Contact Information for Business Card

I want an unique design that make a statement

Number of Pages Required

1 page

Font styles to use

Colors

Designer to choose colors to be used in the design.

Requirements
Must have
• unique design, feel free to modify or change the color of my logo.
Nice to have
• extra design features like spot UV, foil accents, color edges, unique paper, or any thing that would make my card pop.
• I like the feel of the image that I attached

```html
<!DOCTYPE html>
<html lang="en">
<head>
<meta charset="utf-8">
<title>Halvorsen Partners Business Card</title>
<link href="https://fonts.googleapis.com/css2?family=Open+Sans:wght@300;400;600;700&display=swap" rel="stylesheet">
<style>
  :root {
    --backdrop: #3a3a3c;
    --card-dark: #050505;
    --card-light: #f4f4f4;
    --brand-blue: #2f45a8;
    --brand-blue-soft: #4a63c9;
    --steel-grey: #8c8c8e;
    --light-grey: #cfcfcf;
  }
  * { box-sizing: border-box; margin: 0; padding: 0; }
  html, body { width: 1200px; height: 900px; overflow: hidden; }
  body {
    background: var(--backdrop);
    font-family: "Open Sans", Arial, sans-serif;
    display: flex;
    flex-direction: column;
    align-items: center;
    justify-content: center;
    gap: 36px;
  }
  .card {
    width: 700px;
    height: 400px;
    border-radius: 22px;
    position: relative;
    overflow: hidden;
  }
  /* Front side */
  .card--front {
    background: var(--card-dark);
    display: flex;
    flex-direction: column;
    align-items: center;
    justify-content: center;
  }
  .brand {
    display: flex;
    align-items: center;
    gap: 16px;
  }
  .brand__square {
    width: 34px;
    height: 34px;
    background: var(--brand-blue-soft);
  }
  .brand__name {
    font-weight: 600;
    text-transform: uppercase;
    letter-spacing: 1px;
    color: var(--brand-blue-soft);
    font-size: 40px;
    white-space: nowrap;
  }
  .services {
    margin-top: 44px;
    color: var(--light-grey);
    font-size: 17px;
    font-weight: 400;
    letter-spacing: 0.3px;
  }
  .services .divider { margin: 0 10px; }
  .card--front .website {
    margin-top: 26px;
    color: var(--brand-blue-soft);
    font-size: 17px;
  }
  /* Back side */
  .card--back {
    background: linear-gradient(115deg, #ffffff 0%, var(--card-light) 55%, #e6e6e6 100%);
  }
  .card--back .brand {
    position: absolute;
    top: 46px;
    right: 44px;
    gap: 12px;
  }
  .card--back .brand__square { width: 24px; height: 24px; background: var(--brand-blue); }
  .card--back .brand__name { font-size: 26px; color: var(--brand-blue); }
  .person {
    position: absolute;
    top: 150px;
    left: 34px;
    padding-left: 22px;
    border-left: 12px solid var(--brand-blue);
  }
  .person__name {
    font-size: 32px;
    color: var(--steel-grey);
    font-weight: 300;
    line-height: 1.1;
  }
  .person__name strong { font-weight: 700; }
  .person__role {
    font-size: 20px;
    color: var(--brand-blue);
    font-weight: 400;
  }
  .contact {
    position: absolute;
    left: 44px;
    bottom: 62px;
    list-style: none;
    display: flex;
    flex-direction: column;
    gap: 12px;
    color: #333;
    font-size: 18px;
  }
  .contact li { display: flex; align-items: center; gap: 12px; }
  .contact svg { width: 24px; height: 24px; fill: var(--brand-blue); }
  .card-footer {
    position: absolute;
    left: 44px;
    right: 34px;
    bottom: 26px;
    display: flex;
    align-items: flex-end;
    gap: 14px;
  }
  .rule {
    flex: 1;
    height: 3px;
    background: var(--brand-blue);
    margin-bottom: 2px;
  }
  .card--back .website {
    flex: none;
    color: var(--brand-blue);
    font-size: 17px;
    line-height: 1.2;
    white-space: nowrap;
    transform: translateY(-8px);
  }
</style>
</head>
<body>
  <section class="card card--front" aria-label="Card front">
    <div class="brand">
      <span class="brand__square"></span>
      <span class="brand__name">Halvorsen Partners</span>
    </div>
    <p class="services">Site Development<span class="divider">|</span>Utility Construction<span class="divider">|</span>Excavation</p>
    <p class="website">www.HalvorsenSiteworks.example</p>
  </section>

  <section class="card card--back" aria-label="Card back">
    <div class="brand">
      <span class="brand__square"></span>
      <span class="brand__name">Halvorsen Partners</span>
    </div>
    <div class="person">
      <p class="person__name">Marcus <strong>Halvorsen</strong></p>
      <p class="person__role">CEO</p>
    </div>
    <ul class="contact">
      <li>
        <svg viewBox="0 0 24 24" aria-hidden="true"><path d="M2 9c0-3 5-5 10-5s10 2 10 5v2h-5V8.5c-1.5-.6-3.2-.9-5-.9s-3.5.3-5 .9V11H2zM6 12l2-3h8l2 3 2 7H4z"/></svg>
        <span>727-518-6094</span>
      </li>
      <li>
        <svg viewBox="0 0 24 24" aria-hidden="true"><path d="M2 5h20v14H2zm2 2v.5l8 6 8-6V7zm0 3v7h16v-7l-8 6z"/></svg>
        <span>Marcus@HalvorsenSiteworks.example</span>
      </li>
    </ul>
    <div class="card-footer">
      <div class="rule"></div>
      <p class="website">www.HalvorsenSiteworks.example</p>
    </div>
  </section>
</body>
</html>
```